ALL I NEED IS A BUSINESS CARD AND LETTER HEAD OFFICIAL PAPER

i only need a letter head ( sample attached)
along with business cards.
i will upload a sample ,along with the logo of both companies that should be on the letter head and business cards.

Note:its a high end maritime solution company

Company name is Tormund Halvex Africa

slogan : For maritime solution ( it could be on the back side of the business card)

Project Deadline Extended Reason: Hi Guys, thanks for your designs , i am sorry but now we just changed the company name toLuerssen Halvex Africa slogan For Maritime solutions. i hope you can help me with that! slogan could be in the back side or any place, but not next to the title . and both logos of halvex and tormund should be there. thank you Added Sunday, March 1, 2015

Industry/Entity Type

Business

Contact Information for Business Card

as attached, please provide more designs

Font styles to use
Serif

Requirements
Must have
• SAME AS THE BUSINESS LETTER,
• Tormund Halvex Africa
• slogan for Maritime Solutions

```html
<!DOCTYPE html>
<html lang="en">
<head>
<meta charset="utf-8">
<title>Tormund Halvex Africa — Business Card</title>
<link rel="stylesheet" href="https://fonts.googleapis.com/css2?family=Questrial&family=Poiret+One&family=Source+Sans+3:wght@400&display=swap">
<style>
  :root {
    --navy-deep: #0c0a4f;
    --navy: #1d2a86;
    --royal: #2f47a6;
    --sky: #4f8ac6;
    --paper: #ffffff;
    --ink: #111111;
    --caption: #dbe3f6;
    --logo-black: #0a0a0a;
    --logo-blue: #1f3d8f;
  }
  html, body {
    margin: 0;
    padding: 0;
    width: 1200px;
    height: 687px;
    overflow: hidden;
    background: var(--paper);
  }
  .card {
    position: relative;
    width: 1200px;
    height: 687px;
    overflow: hidden;
    background: var(--paper);
  }
  .card__bands {
    position: absolute;
    inset: 0;
    width: 1200px;
    height: 687px;
  }
  .company {
    position: absolute;
    left: 78px;
    top: 36px;
    margin: 0;
    color: var(--paper);
    font-family: "Questrial", sans-serif;
    font-weight: 400;
    font-variant: small-caps;
    font-size: 26px;
    letter-spacing: 4px;
    line-height: 38px;
  }
  .company__slogan { display: block; }
  .address {
    position: absolute;
    left: 72px;
    top: 134px;
    margin: 0;
    color: var(--caption);
    font-family: "Poiret One", sans-serif;
    font-size: 17px;
    letter-spacing: 0.3px;
  }
  .brand {
    position: absolute;
    top: 41px;
    height: 67px;
    display: flex;
    align-items: center;
    justify-content: center;
    font-family: "Questrial", sans-serif;
    font-weight: 400;
    letter-spacing: 2px;
  }
  .brand--tormund {
    left: 712px;
    width: 256px;
    background: var(--logo-black);
    color: var(--paper);
    font-size: 34px;
  }
  .brand--halvex {
    left: 968px;
    width: 178px;
    background: var(--paper);
    color: var(--logo-blue);
    font-size: 24px;
    gap: 10px;
  }
  .brand__square {
    width: 30px;
    height: 30px;
    background: var(--logo-blue);
  }
  .holder {
    position: absolute;
    left: 38px;
    top: 268px;
    width: 450px;
    margin: 0;
    text-align: center;
    color: var(--ink);
    font-family: "Source Sans 3", sans-serif;
    font-weight: 400;
    font-size: 50px;
    line-height: 68px;
  }
  .holder__title { display: block; }
  .contact {
    position: absolute;
    left: 716px;
    top: 256px;
    margin: 0;
    padding: 0;
    list-style: none;
    color: var(--ink);
    font-family: "Poiret One", sans-serif;
    font-size: 35px;
    line-height: 57px;
  }
</style>
</head>
<body>
  <main class="card">
    <svg class="card__bands" viewBox="0 0 1051 602" preserveAspectRatio="none" aria-hidden="false">
      <defs>
        <linearGradient id="top-band" x1="0" y1="0" x2="1" y2="0">
          <stop offset="0" stop-color="#2a3796"/>
          <stop offset="0.35" stop-color="#2e4aa4"/>
          <stop offset="0.62" stop-color="#4f8ac6"/>
          <stop offset="0.85" stop-color="#1d2a86"/>
          <stop offset="1" stop-color="#0c0a4f"/>
        </linearGradient>
        <linearGradient id="bottom-band" x1="0" y1="0" x2="1" y2="0">
          <stop offset="0" stop-color="#1b2077"/>
          <stop offset="0.48" stop-color="#4f8ac6"/>
          <stop offset="0.75" stop-color="#1d2a86"/>
          <stop offset="1" stop-color="#0c0a4f"/>
        </linearGradient>
      </defs>
      <path class="band band--top" role="img" aria-label="Blue header band with fine flowing wave lines"
            fill="url(#top-band)"
            d="M0,0 H1051 V145 C1035,185 995,196 960,186 C900,168 840,150 700,150 C500,150 300,160 150,180 C95,187 45,186 0,186 Z"/>
      <path class="band band--bottom" fill="url(#bottom-band)"
            d="M1051,336 C1030,330 1022,378 1002,410 C955,480 800,512 600,512 C400,512 150,502 45,566 C22,582 10,594 0,602 H1051 Z"/>
    </svg>

    <h1 class="company">Tormund Halvex Africa<span class="company__slogan">For Maritime Solutions</span></h1>
    <p class="address">P.O.BOX 400210 Abu Dhabi-UAE</p>

    <div class="brand brand--tormund">TORMUND</div>
    <div class="brand brand--halvex"><span class="brand__square"></span>HALVEX</div>

    <p class="holder">John Doe<span class="holder__title">Regional Manager</span></p>

    <ul class="contact">
      <li>Phone: +971 2 555 0130</li>
      <li>Fax: +971 2 555 0131</li>
      <li>Email: info@halvex1.ae</li>
    </ul>
  </main>
</body>
</html>
```